DORIVAN
ENERGY FOR TOMORROW
Professional
Tobin Rasquelle
2417 Fennimore Lane
Glen Burnie, MD 21060
tobin@dorivan7.com
www.dorivan7.com
I can provide logo as need it.
Logo and write this underneath the logo or where you think it will look better.
Have fun!!

```html
<!DOCTYPE html>
<html lang="en">
<head>
<meta charset="UTF-8">
<title>Dorivan Stationery</title>
<link rel="stylesheet" href="https://fonts.googleapis.com/css2?family=Montserrat:wght@400;600&display=swap">
<style>
:root{
  --bg:#e9ebee;
  --paper:#ffffff;
  --blue:#1f6fc0;
  --blue-dark:#124f95;
  --green:#4cb848;
  --yellow:#f6ec6a;
  --ink:#3a3f47;
  --muted:#7d848e;
}
*{margin:0;padding:0;box-sizing:border-box}
html,body{width:1200px;height:464px;overflow:hidden}
body{background:var(--bg);font-family:"Montserrat",Arial,sans-serif;color:var(--ink);position:relative}
.sheet{position:absolute;background:var(--paper);box-shadow:0 2px 8px rgba(0,0,0,.18);overflow:hidden}
.band{position:absolute;left:0;top:0;width:100%;background:var(--blue);border-bottom:3px solid var(--green)}
.brand{font-weight:600;color:var(--blue);letter-spacing:1px;line-height:1}
.tagline{font-weight:400;color:var(--green);text-transform:uppercase;letter-spacing:1.5px;line-height:1}

/* business cards */
.card{width:210px;height:120px}
.card-front{left:36px;top:86px}
.card-front .brand{position:absolute;left:20px;top:30px;font-size:24px}
.card-front .tagline{position:absolute;left:20px;top:60px;font-size:7px}
.card-front .strip{position:absolute;left:0;bottom:14px;width:100%;height:26px;background:var(--yellow)}
.card-front .base{position:absolute;left:0;bottom:0;width:100%;height:14px;background:var(--blue)}
.card-back{left:36px;top:246px}
.card-back .band{height:22px}
.card-back .brand{position:absolute;left:14px;top:44px;font-size:16px}
.card-back .tagline{position:absolute;left:14px;top:64px;font-size:5px}
.card-back .contact{position:absolute;right:12px;top:34px;text-align:right;font-size:6.5px;line-height:1.55;color:var(--ink)}
.card-back .contact .name{font-weight:600;font-size:8px;color:var(--blue-dark)}
.card-back .contact .role{color:var(--muted)}

/* letterheads */
.letter{width:262px;height:370px;top:46px}
.letter-first{left:282px}
.letter-second{left:572px}
.letter .band{height:28px}
.letter .brand{position:absolute;left:18px;top:44px;font-size:19px}
.letter .tagline{position:absolute;left:18px;top:66px;font-size:6px}
.letter .head-contact{position:absolute;right:14px;top:7px;text-align:right;font-size:5.5px;line-height:1.5;color:#fff}
.letter .footer{position:absolute;left:0;bottom:0;width:100%;padding:7px 0;text-align:center;font-size:5.5px;color:var(--muted);border-top:2px solid var(--green)}

/* envelope */
.envelope{left:870px;top:150px;width:296px;height:156px}
.envelope .band{height:18px}
.envelope .brand{position:absolute;left:16px;top:34px;font-size:16px}
.envelope .tagline{position:absolute;left:16px;top:54px;font-size:5px}
.envelope .return{position:absolute;left:16px;top:66px;font-size:5.5px;line-height:1.5;color:var(--muted)}
.envelope .base{position:absolute;left:0;bottom:0;width:100%;height:6px;background:var(--green)}
</style>
</head>
<body>

<div class="sheet card card-front">
  <div class="brand">DORIVAN</div>
  <div class="tagline">Energy for Tomorrow</div>
  <div class="strip"></div>
  <div class="base"></div>
</div>

<div class="sheet card card-back">
  <div class="band"></div>
  <div class="brand">DORIVAN</div>
  <div class="tagline">Energy for Tomorrow</div>
  <div class="contact">
    <div class="name">Tobin Rasquelle</div>
    <div class="role">Sales Director</div>
    <div>2417 Fennimore Lane</div>
    <div>Glen Burnie, MD 21060</div>
    <div>tobin@dorivan7.com</div>
    <div>www.dorivan7.com</div>
  </div>
</div>

<div class="sheet letter letter-first">
  <div class="band"></div>
  <div class="head-contact">
    <div>2417 Fennimore Lane</div>
    <div>Glen Burnie, MD 21060</div>
  </div>
  <div class="brand">DORIVAN</div>
  <div class="tagline">Energy for Tomorrow</div>
  <div class="footer">tobin@dorivan7.com &nbsp;|&nbsp; www.dorivan7.com</div>
</div>

<div class="sheet letter letter-second">
  <div class="band"></div>
  <div class="brand">DORIVAN</div>
  <div class="tagline">Energy for Tomorrow</div>
  <div class="footer">2417 Fennimore Lane, Glen Burnie, MD 21060</div>
</div>

<div class="sheet envelope">
  <div class="band"></div>
  <div class="brand">DORIVAN</div>
  <div class="tagline">Energy for Tomorrow</div>
  <div class="return">
    <div>2417 Fennimore Lane</div>
    <div>Glen Burnie, MD 21060</div>
  </div>
  <div class="base"></div>
</div>

</body>
</html>
```